distributor of aftermarket auto electrical components

I am after business card design for my new company called
Summit Vehicle Supplies (SVS as the acronym). I will supplying automotive wiring components, basically from battery to headlight. I will be aiming to sell in the 4wd scene and to auto electricians. i am not worried which colours are used though i would like it to be dynamic.
Updates

sorry guys, i have add a mobile and e-mail address that will need to on there as well. Sorry for theĀ inconvenience.

sorry guys i had erred on my spelling with my e-mail. i have now fixed it in the brief

Target Market(s)

4wd industry, custom cars, RV, auto electricians

Industry/Entity Type

Electrical

Requirements
Must have
• Company Name
ABN number: 71 306 548 290
Director: Derek Holloway
M 0432 718 946
E dhollo@fernwire.com.au

```html
<!DOCTYPE html>
<html lang="en">
<head>
<meta charset="utf-8">
<title>Summit Vehicle Supplies – Business Card</title>
<link rel="stylesheet" href="https://fonts.googleapis.com/css2?family=Arimo:wght@400;700&display=swap">
<style>
  :root {
    --page: #ffffff;
    --navy: #0b3563;
    --blue: #1170b8;
    --deep-blue: #0d4a86;
    --black: #0a0a0a;
    --steel-dark: #4a4a4c;
    --steel-light: #d8d8d8;
    --orange: #f5a833;
    --ink-blue: #0d3f73;
    --ink-grey: #555a60;
    --white: #ffffff;
  }
  * { margin: 0; padding: 0; box-sizing: border-box; }
  html, body {
    width: 1200px; height: 901px; overflow: hidden;
    background: var(--page);
    font-family: "Arimo", Arial, sans-serif;
  }
  .card {
    position: absolute; left: 301px; width: 595px; height: 340px;
    overflow: hidden;
    box-shadow: 2px 3px 6px rgba(0,0,0,0.35);
  }
  .card-front { top: 71px; background: linear-gradient(200deg, var(--blue) 0%, var(--deep-blue) 45%, var(--navy) 100%); }
  .card-back { top: 489px; background: linear-gradient(150deg, #e6e7e9 0%, #ffffff 40%); }
  .card-art { position: absolute; inset: 0; width: 595px; height: 340px; }

  .brand { position: absolute; text-align: center; }
  .brand-mark {
    display: flex; align-items: center; justify-content: center; gap: 12px;
    font-weight: 700; font-size: 62px; line-height: 1; letter-spacing: 4px;
  }
  .brand-dot { width: 16px; height: 16px; border-radius: 50%; background: var(--orange); }
  .brand-name { font-weight: 700; margin-top: 14px; white-space: nowrap; }

  .card-front .brand { left: 0; right: 0; top: 105px; }
  .card-front .brand-mark { color: var(--white); }
  .card-front .brand-name { color: var(--white); font-size: 20px; }

  .card-back .brand { left: 280px; width: 276px; top: 60px; }
  .card-back .brand-mark { color: var(--ink-blue); font-size: 54px; }
  .card-back .brand-name { color: #7d8185; font-size: 17px; margin-top: 10px; }

  .holder { position: absolute; left: 38px; top: 123px; }
  .holder-name { color: var(--ink-blue); font-weight: 700; font-size: 19px; }
  .holder-role { color: var(--ink-grey); font-size: 15px; margin-top: 3px; }

  .contact { position: absolute; left: 38px; top: 186px; list-style: none; }
  .contact li {
    display: flex; align-items: center; gap: 8px;
    color: var(--ink-grey); font-size: 15px; height: 20px;
  }
  .contact svg { width: 12px; height: 12px; flex: none; }

  .abn { position: absolute; right: 30px; top: 303px; color: var(--white); font-size: 15px; }
</style>
</head>
<body>

<section class="card card-front" aria-label="Card front">
  <svg class="card-art" viewBox="0 0 595 340" aria-hidden="true">
    <defs>
      <linearGradient id="steelFront" x1="0" x2="1" y1="0" y2="0">
        <stop offset="0" stop-color="#5a5a5c"/>
        <stop offset="0.55" stop-color="#e4e4e4"/>
        <stop offset="1" stop-color="#3d3d3f"/>
      </linearGradient>
    </defs>
    <path d="M0,255 Q300,330 595,225 L595,340 L0,340 Z" fill="url(#steelFront)"/>
    <path d="M0,282 Q300,345 595,245 L595,340 L0,340 Z" fill="var(--black)"/>
  </svg>
  <div class="brand">
    <div class="brand-mark">SVS<span class="brand-dot"></span></div>
    <div class="brand-name">Summit Vehicle Supplies</div>
  </div>
</section>

<section class="card card-back" aria-label="Card back">
  <svg class="card-art" viewBox="0 0 595 340" aria-hidden="true">
    <defs>
      <linearGradient id="steelBack" x1="0" x2="1" y1="0" y2="0">
        <stop offset="0" stop-color="#4f4f51"/>
        <stop offset="0.5" stop-color="#dcdcdc"/>
        <stop offset="1" stop-color="#5a5a5c"/>
      </linearGradient>
      <linearGradient id="blueBack" x1="0" x2="1" y1="0" y2="0">
        <stop offset="0" stop-color="#0f5da3"/>
        <stop offset="0.35" stop-color="#1170b8"/>
        <stop offset="1" stop-color="#0b3563"/>
      </linearGradient>
    </defs>
    <path d="M0,228 Q300,315 595,195 L595,340 L0,340 Z" fill="url(#steelBack)"/>
    <path d="M0,255 Q300,320 595,212 L595,340 L0,340 Z" fill="url(#blueBack)"/>
  </svg>

  <div class="holder">
    <div class="holder-name">Derek Holloway</div>
    <div class="holder-role">Director</div>
  </div>

  <ul class="contact">
    <li>
      <svg viewBox="0 0 12 12" aria-hidden="true"><rect x="3" y="0.5" width="6" height="11" rx="1.2" fill="none" stroke="var(--orange)" stroke-width="1.4"/><rect x="4.3" y="2" width="3.4" height="5" fill="var(--orange)"/></svg>
      0432 718 946
    </li>
    <li>
      <svg viewBox="0 0 12 12" aria-hidden="true"><rect x="0.5" y="2" width="11" height="8" fill="var(--orange)"/><path d="M0.5,2 L6,6.5 L11.5,2" fill="none" stroke="#fff" stroke-width="1"/></svg>
      dhollo@fernwire.com.au
    </li>
  </ul>

  <div class="brand">
    <div class="brand-mark">SVS<span class="brand-dot"></span></div>
    <div class="brand-name">Summit Vehicle Supplies</div>
  </div>

  <div class="abn">ABN number: 71 306 548 290</div>
</section>

</body>
</html>
```